Good Morning Banner

We need a banner design (20.4 x 10.14) with the words 'Good Morning' as the main feature and the words 'Pastor R.K. Adeyemi-Lowe' underneath. Attached is an example but let your creative juices flow!

Target Market(s)

Christian

```html
<!DOCTYPE html>
<html lang="en">
<head>
<meta charset="utf-8">
<title>Good Morning Banner</title>
<link rel="stylesheet" href="https://fonts.googleapis.com/css2?family=Poppins:wght@400;500;700&display=swap">
<style>
  :root {
    --page-bg: #e9ebec;
    --sky-light: #e8e6a8;
    --sky-mid: #a8a554;
    --sky-dark: #4a4a1c;
    --sun: #fff7c4;
    --rock: #141408;
    --footer-bg: #2b3a0c;
    --gold: #e2bb1c;
    --gold-light: #f6df4a;
    --ink: #0a0a06;
    --white: #ffffff;
  }
  * { margin: 0; padding: 0; box-sizing: border-box; }
  html, body {
    width: 1200px; height: 923px; overflow: hidden;
    background: var(--page-bg);
    font-family: "Poppins", sans-serif;
  }
  .banner {
    position: absolute; left: 50px; top: 186px;
    width: 1103px; height: 550px; overflow: hidden;
    box-shadow: 0 6px 24px rgba(0,0,0,0.18);
  }
  .banner__photo {
    position: absolute; inset: 0 0 54px 0;
    background:
      radial-gradient(circle at 60% 33%, var(--sun) 0, rgba(255,240,150,0.85) 6%, rgba(230,220,120,0) 26%),
      linear-gradient(to bottom, var(--sky-dark) 0%, var(--sky-mid) 30%, var(--sky-light) 55%, #8c8a3a 68%, var(--rock) 80%, var(--rock) 100%);
  }
  .banner__title {
    position: absolute; left: 0; top: 0;
    width: 1103px; height: 180px;
    overflow: visible;
    filter: drop-shadow(0 0 3px rgba(255,255,235,0.95)) drop-shadow(0 0 8px rgba(255,255,220,0.6));
  }
  .banner__title text {
    font-family: "Poppins", sans-serif;
    font-weight: 700; font-size: 166px;
  }
  .banner__name {
    position: absolute; right: 30px; top: 190px;
    font-weight: 500; font-size: 28px; letter-spacing: -0.01em;
    color: var(--gold);
    white-space: nowrap;
    text-shadow: 0 0 2px #3a2c00, 0 1px 3px rgba(0,0,0,0.6);
  }
  .banner__footer {
    position: absolute; left: 0; right: 0; bottom: 0; height: 54px;
    background: var(--footer-bg);
    display: flex; align-items: center; justify-content: space-between;
    padding: 0 22px 0 15px; color: var(--white);
  }
  .brand { font-weight: 700; font-size: 33px; letter-spacing: -0.03em; }
  .contacts { display: flex; align-items: center; gap: 28px; font-size: 23px; font-weight: 400; }
  .contact { display: flex; align-items: center; gap: 6px; }
  .contact svg { width: 24px; height: 24px; }
</style>
</head>
<body>
  <section class="banner">
    <div class="banner__photo" role="img" aria-label="Silhouette of one climber helping another up a rocky hilltop against a bright golden sunrise sky"></div>
    <h1 class="banner__heading">
      <svg class="banner__title" viewBox="0 0 1103 180" aria-label="GOODmorning" role="img">
        <defs>
          <linearGradient id="title-fill" gradientUnits="userSpaceOnUse" x1="28" y1="0" x2="1076" y2="0">
            <stop offset="0" stop-color="#0a0a06"/>
            <stop offset="0.34" stop-color="#0a0a06"/>
            <stop offset="0.40" stop-color="#6a5200"/>
            <stop offset="0.50" stop-color="#e2bb1c"/>
            <stop offset="0.62" stop-color="#f6df4a"/>
            <stop offset="0.72" stop-color="#e2bb1c"/>
            <stop offset="0.80" stop-color="#0a0a06"/>
            <stop offset="1" stop-color="#0a0a06"/>
          </linearGradient>
        </defs>
        <text x="28" y="132" textLength="1048" lengthAdjust="spacingAndGlyphs" fill="url(#title-fill)">GOODmorning</text>
      </svg>
    </h1>
    <p class="banner__name">PASTOR R.K. ADEYEMI-LOWE</p>
    <footer class="banner__footer">
      <span class="brand">dawnlight.tv</span>
      <div class="contacts">
        <span class="contact">
          <svg viewBox="0 0 24 24" fill="none" stroke="currentColor" stroke-width="1.4" aria-hidden="true">
            <circle cx="12" cy="12" r="10"/>
            <ellipse cx="12" cy="12" rx="4.5" ry="10"/>
            <line x1="2" y1="12" x2="22" y2="12"/>
            <path d="M4 6.5h16M4 17.5h16"/>
          </svg>
          www.dawnlight.tv
        </span>
        <span class="contact">
          <svg viewBox="0 0 24 24" fill="none" stroke="currentColor" stroke-width="1.4" aria-hidden="true">
            <circle cx="12" cy="12" r="10"/>
          </svg>
          rkaministries
        </span>
      </div>
    </footer>
  </section>
</body>
</html>
```